The Pixel Tap Business card.

A Simple card with our Logo and contact information. To give to investors and other professionals.

We are a nerd themed bar.
our target market is young professionals age 21+ but the real purpose of this business card is to present to potential investors and other professionals with our contact information. as we are still looking for funding before we start up.

I am partial to green and my partner likes red we are open to iteration.

Target Market(s)

Investors

Industry/Entity Type

Business

Contact Information for Business Card

Martin Hale (225) 730-6192 kent.h4711@mailnest.test Glen Porter (225) 968-5037 glenp318@mailnest.test

Font styles to use
Serif

Requirements
Nice to have
• Keep it simple but not boring.
• Use the Logos but feel free to edit them to match theme/colors.
• Keep the back clean and use one of the Logos.

```html
<!DOCTYPE html>
<html lang="en">
<head>
<meta charset="utf-8">
<title>The Pixel Tap – Business Card</title>
<link href="https://fonts.googleapis.com/css2?family=Open+Sans:wght@400;600;700;800&display=swap" rel="stylesheet">
<style>
  :root {
    --page-bg: #ececec;
    --card-bg: #f4f4f5;
    --ink: #141414;
    --ink-soft: #4a4a4a;
    --accent-red: #d3222c;
  }
  * { box-sizing: border-box; margin: 0; padding: 0; }
  html, body {
    width: 1105px;
    height: 1200px;
    overflow: hidden;
    background: var(--page-bg);
    font-family: "Open Sans", Arial, sans-serif;
  }
  .canvas {
    position: relative;
    width: 1105px;
    height: 1200px;
  }
  .card {
    position: absolute;
    left: 182px;
    width: 746px;
    height: 425px;
    background: var(--card-bg);
  }
  .card--front { top: 119px; }
  .card--back { top: 637px; }

  .contact {
    position: absolute;
    right: 47px;
    top: 40px;
    text-align: right;
    color: var(--ink-soft);
  }
  .contact__name {
    font-size: 25px;
    font-weight: 600;
    color: var(--ink);
    letter-spacing: 0.2px;
    margin-right: 0;
    margin-bottom: 22px;
  }
  .contact__line {
    display: flex;
    justify-content: flex-end;
    align-items: center;
    gap: 20px;
    font-size: 18px;
    height: 34px;
  }
  .contact__icon {
    width: 18px;
    height: 18px;
    flex: none;
  }

  .brand {
    position: absolute;
    display: flex;
    align-items: center;
    gap: 16px;
    color: var(--ink);
    font-weight: 800;
    text-transform: uppercase;
    letter-spacing: 1px;
    white-space: nowrap;
  }
  .brand__dot {
    flex: none;
    border-radius: 50%;
    background: var(--accent-red);
  }
  .card--front .brand {
    right: 47px;
    top: 275px;
    font-size: 46px;
  }
  .card--front .brand__dot { width: 34px; height: 34px; }
  .card--back .brand {
    left: 50%;
    top: 50%;
    transform: translate(-50%, -50%);
    font-size: 44px;
  }
  .card--back .brand__dot { width: 32px; height: 32px; }
</style>
</head>
<body>
<main class="canvas">
  <section class="card card--front" aria-label="Business card front">
    <div class="contact">
      <p class="contact__name">MARTIN HALE</p>
      <p class="contact__line">
        <span>(225) 730-6192</span>
        <svg class="contact__icon" viewBox="0 0 18 18" aria-hidden="true">
          <rect x="4.5" y="1" width="9" height="16" rx="1.5" fill="none" stroke="#141414" stroke-width="1.8"/>
          <line x1="7.5" y1="14.2" x2="10.5" y2="14.2" stroke="#141414" stroke-width="1.4"/>
        </svg>
      </p>
      <p class="contact__line">
        <span>kent.h4711@mailnest.test</span>
        <svg class="contact__icon" viewBox="0 0 18 18" aria-hidden="true">
          <rect x="1" y="4" width="16" height="11" fill="#141414"/>
          <polyline points="1.5,4.5 9,10 16.5,4.5" fill="none" stroke="#f4f4f5" stroke-width="1.3"/>
        </svg>
      </p>
    </div>
    <div class="brand">
      <span class="brand__dot" aria-hidden="true"></span>
      <span class="brand__name">The Pixel Tap</span>
    </div>
  </section>

  <section class="card card--back" aria-label="Business card back">
    <div class="brand">
      <span class="brand__dot" aria-hidden="true"></span>
      <span class="brand__name">The Pixel Tap</span>
    </div>
  </section>
</main>
</body>
</html>
```